Accident Law Firm Billboard Bold Easy to See Car Accidents

We need a billboard design that can catch attention in a very crowed Car Accident lawyer market. We wish to feature the phone number (652) 318-4470 as the focus of the Bill Board. We are trying to get the phone number recognized and remembered by drivers. The law firm name is not as crucial to remember.
Basically, It's CAR ACCIDENT? Then (652) 318-4470. We are not married to any specific color scheme but it has to POP and catch attention.
So the Crucial elements are as follows:
1. Phone number (652) 318-4470
2. Words CAR ACCIDENT?
3. Firm Logo in lower portion or where appropriate. Firm Logo to be provided
4. We may want to try a Day Glow orange color, with White and Black added. An example of the color scheme shall be provided.
5. Possible "Catch Phrase" to be used, "It's Time Call 9"
Target Market(s)
Orlando Florida Car Accident victims
Industry/Entity Type
Law Firm
Requirements
Must have
- Easy to see phone number (652) 318-4470
- Catch attention
Nice to have
- I would like to have the sign visible in bright sunlight and it not too hard to immediately know what phone number is for
Should not have
- too many words
- No bold enough
- confusing fonts
- Unclear fonts

```html
<!DOCTYPE html>
<html lang="en">
<head>
<meta charset="UTF-8">
<title>Marlowe Law Firm – Car Accident Billboard</title>
<link href="https://fonts.googleapis.com/css2?family=Anton&family=Montserrat:wght@600&family=Oswald:wght@500;700&display=swap" rel="stylesheet">
<style>
  :root {
    --orange-light: #f9a12a;
    --orange: #f47b20;
    --orange-deep: #ef5a22;
    --black: #050505;
    --white: #ffffff;
    --page: #ffffff;
  }
  html, body {
    margin: 0;
    padding: 0;
    width: 880px;
    height: 1200px;
    overflow: hidden;
    background: var(--page);
  }
  .canvas {
    position: relative;
    width: 880px;
    height: 1200px;
  }
  .billboard {
    position: absolute;
    left: 40px;
    top: 332px;
    width: 800px;
    height: 535px;
    background: var(--black);
    box-shadow: 14px 16px 12px rgba(0, 0, 0, 0.35);
    overflow: hidden;
  }
  .billboard__bands {
    position: absolute;
    inset: 0;
    width: 100%;
    height: 100%;
  }
  .firm-name {
    position: absolute;
    left: 0;
    right: 0;
    top: 26px;
    margin: 0;
    text-align: center;
    color: var(--white);
    font-family: "Montserrat", sans-serif;
    font-weight: 600;
    line-height: 1;
  }
  .firm-name__main {
    display: block;
    font-size: 45px;
    letter-spacing: 1px;
  }
  .firm-name__sub {
    display: block;
    margin-top: 4px;
    font-size: 24px;
    letter-spacing: 5px;
  }
  .headline {
    position: absolute;
    left: 0;
    right: 0;
    top: 176px;
    margin: 0;
    text-align: center;
    font-family: "Anton", sans-serif;
    font-size: 92px;
    line-height: 1;
    letter-spacing: 4px;
    color: var(--orange);
    font-weight: 400;
  }
  .headline__mark {
    color: var(--white);
  }
  .phone {
    position: absolute;
    left: 32px;
    top: 298px;
    display: flex;
    align-items: center;
    gap: 16px;
  }
  .phone__icon {
    width: 58px;
    height: 58px;
    flex: none;
  }
  .phone__number {
    font-family: "Anton", sans-serif;
    font-size: 96px;
    line-height: 1;
    color: var(--white);
    text-shadow: 3px 3px 0 var(--orange-deep);
    letter-spacing: 1px;
  }
  .tagline {
    position: absolute;
    left: 170px;
    width: 461px;
    top: 466px;
    height: 69px;
    margin: 0;
    display: flex;
    align-items: center;
    justify-content: center;
    gap: 10px;
    color: var(--white);
    font-family: "Oswald", sans-serif;
    font-size: 36px;
    line-height: 1;
  }
  .tagline__lead { font-weight: 500; }
  .tagline__call { font-weight: 700; }
</style>
</head>
<body>
<main class="canvas">
  <section class="billboard">
    <svg class="billboard__bands" viewBox="0 0 800 535" aria-hidden="true">
      <defs>
        <linearGradient id="bandGradient" x1="0" y1="0" x2="0" y2="1">
          <stop offset="0" stop-color="#f9a12a"/>
          <stop offset="1" stop-color="#ef5a22"/>
        </linearGradient>
      </defs>
      <path class="band band--top" fill="url(#bandGradient)"
            d="M26 0 L773 0 L660 106 Q632 130 596 130 L204 130 Q168 130 140 106 Z"/>
      <path class="band band--bottom" fill="url(#bandGradient)"
            d="M170 535 L222 482 Q236 466 258 466 L540 466 Q562 466 576 482 L631 535 Z"/>
    </svg>

    <div class="firm-name">
      <span class="firm-name__main">MARLOWE</span>
      <span class="firm-name__sub">LAW FIRM P.C.</span>
    </div>

    <h1 class="headline">CAR ACCIDENT<span class="headline__mark">?</span></h1>

    <div class="phone">
      <svg class="phone__icon" viewBox="0 0 60 60" aria-hidden="true">
        <path fill="#f47b20" d="M14 6 Q8 8 7 16 Q6 34 24 50 Q34 58 42 56 Q48 54 50 48 L41 38 Q38 36 35 39 L32 42 Q24 37 19 28 L22 25 Q25 22 23 19 Z"/>
        <path fill="none" stroke="#ffffff" stroke-width="3" stroke-linecap="round" d="M33 22 Q38 24 39 30"/>
        <path fill="none" stroke="#ffffff" stroke-width="3" stroke-linecap="round" d="M35 14 Q45 18 47 28"/>
        <path fill="none" stroke="#ffffff" stroke-width="3" stroke-linecap="round" d="M37 6 Q52 11 55 26"/>
      </svg>
      <span class="phone__number">(652) 318-4470</span>
    </div>

    <p class="tagline"><span class="tagline__lead">It's Time</span><span class="tagline__call">Call 9</span></p>
  </section>
</main>
</body>
</html>
```